IT Consulting, IT Guru, Software Development, Network Solutions, Hosting

Attached is logo for our company, we just was the designers to come up with creative ideas to use the logo and the theme to come with creative and energetic business cards that leave an impression and stick in people's head.

Target Market(s)

Medical, Law, Entertainment, Real estate, any small to medium size business.

Industry/Entity Type

Business

Font styles to use
Serif
Sans Serif

```html
<!DOCTYPE html>
<html lang="en">
<head>
<meta charset="utf-8">
<title>Byteward Business Cards</title>
<link rel="stylesheet" href="https://fonts.googleapis.com/css2?family=Arvo:wght@700&family=Lato:wght@400;700&display=swap">
<style>
  :root {
    --page: #e6e8ea;
    --card: #3e3e3e;
    --card-shadow: #343434;
    --note: #ffcc0a;
    --note-fold: #f6efd6;
    --note-fold-shade: #d8a523;
    --ink: #3a3a3a;
    --muted: #6a6a6a;
    --brand: #d9d9d9;
    --circle: #5a5a5a;
  }
  * { box-sizing: border-box; margin: 0; padding: 0; }
  html, body { width: 1200px; height: 900px; overflow: hidden; }
  body { background: var(--page); position: relative; font-family: "Lato", sans-serif; }

  .card {
    position: absolute;
    width: 590px;
    height: 355px;
    background: var(--card);
    overflow: hidden;
    box-shadow: 0 10px 24px rgba(0,0,0,0.25);
  }
  .card--front { left: 40px; top: 90px; }
  .card--back { left: 570px; top: 465px; }

  .card__shadow { position: absolute; inset: 0; }

  .note {
    position: absolute;
    background: var(--note);
  }
  .note__fold { position: absolute; right: 0; bottom: 0; }
  .note__title {
    font-family: "Arvo", serif;
    font-weight: 700;
    color: var(--ink);
    position: absolute;
    white-space: nowrap;
  }

  .card--front .note { left: 60px; top: 50px; width: 250px; height: 255px; }
  .card--front .note__title { left: 24px; top: 48px; font-size: 28px; }

  .contact-list { position: absolute; left: 22px; top: 128px; list-style: none; }
  .contact-list li {
    display: flex; align-items: center; gap: 9px;
    font-size: 11.5px; color: var(--ink);
    height: 25px;
  }
  .contact-list svg { width: 10px; height: 10px; fill: var(--ink); flex: none; }

  .brand {
    position: absolute;
    font-family: "Lato", sans-serif;
    font-weight: 400;
    color: var(--brand);
    letter-spacing: 1px;
    white-space: nowrap;
  }
  .card--front .brand { left: 355px; top: 46px; font-size: 32px; }

  .social { position: absolute; left: 360px; display: flex; align-items: center; gap: 14px; }
  .social--first { top: 97px; }
  .social--second { top: 180px; }
  .social__mark { width: 50px; height: 50px; border-radius: 50%; background: var(--circle); }
  .social__link { font-size: 13px; font-weight: 700; color: var(--muted); margin-top: -18px; }

  .card--back .brand { left: 0; right: 0; top: 52px; text-align: center; font-size: 32px; }
  .card--back .note { left: 198px; top: 105px; width: 200px; height: 170px; }
  .card--back .note__title { left: 22px; top: 68px; font-size: 21px; }
</style>
</head>
<body>

  <section class="card card--front">
    <svg class="card__shadow" width="590" height="355" viewBox="0 0 590 355">
      <polygon points="60,50 0,110 0,355 240,355 310,305 60,305" fill="var(--card-shadow)"/>
    </svg>
    <div class="note">
      <h2 class="note__title">Get in touch</h2>
      <ul class="contact-list">
        <li><svg viewBox="0 0 10 10"><path d="M5 0a3.5 3.5 0 0 1 3.5 3.5C8.5 6 5 10 5 10S1.5 6 1.5 3.5A3.5 3.5 0 0 1 5 0zm0 2a1.5 1.5 0 1 0 0 3a1.5 1.5 0 0 0 0-3z"/></svg>Address 54321</li>
        <li><svg viewBox="0 0 10 10"><path d="M0 2h10v6H0zM0 2l5 3.5L10 2" stroke="var(--note)" stroke-width="0.8"/></svg>mail@youremail.com</li>
        <li><svg viewBox="0 0 10 10"><circle cx="5" cy="5" r="4.5"/><path d="M0.5 5h9M5 0.5v9M5 0.5c-2.5 2.5-2.5 6.5 0 9M5 0.5c2.5 2.5 2.5 6.5 0 9" stroke="var(--note)" stroke-width="0.6" fill="none"/></svg>www.yourwebsite.com</li>
        <li><svg viewBox="0 0 10 10"><path d="M2 0.5l2 2.2-1 1.3c.7 1.4 1.6 2.3 3 3l1.3-1 2.2 2-1.2 1.6C4.7 9.4.6 5.3.4 1.7z"/></svg>+000 - 1234 - 5678</li>
      </ul>
      <svg class="note__fold" width="44" height="44" viewBox="0 0 44 44">
        <polygon points="44,0 44,44 0,44" fill="var(--card-shadow)"/>
        <polygon points="44,0 0,44 12,14" fill="var(--note-fold-shade)"/>
        <polygon points="44,0 0,44 30,30" fill="var(--note-fold)"/>
      </svg>
    </div>

    <p class="brand">BYTEWARD</p>

    <div class="social social--first">
      <span class="social__mark" role="img" aria-label="Social network icon"></span>
      <span class="social__link">linkbook.net</span>
    </div>
    <div class="social social--second">
      <span class="social__mark" role="img" aria-label="Social network icon"></span>
      <span class="social__link">chirpline.net</span>
    </div>
  </section>

  <section class="card card--back">
    <svg class="card__shadow" width="590" height="355" viewBox="0 0 590 355">
      <polygon points="198,105 158,135 158,305 330,305 398,275 198,275" fill="var(--card-shadow)"/>
    </svg>
    <p class="brand">BYTEWARD</p>
    <div class="note">
      <h2 class="note__title">Get in touch</h2>
      <svg class="note__fold" width="38" height="38" viewBox="0 0 38 38">
        <polygon points="38,0 38,38 0,38" fill="var(--card-shadow)"/>
        <polygon points="38,0 0,38 10,12" fill="var(--note-fold-shade)"/>
        <polygon points="38,0 0,38 26,26" fill="var(--note-fold)"/>
      </svg>
    </div>
  </section>

</body>
</html>
```